Stationery Design Project

We are a packaging machinery manufacturer that mainly serve the food industry.
We now require a full set of stationary including name card, envelop, letter paper, and etc. to match our company image. The logo has been awarded in a previous contest which is attached here.
Updates
Project Deadline Extended
Reason: We have extended the deadline. We have adjusted the deadline before launch to avoid confusion but it turns out the new date wasn't implemented by the system. All designers please feel free to submit your design. Thank you!
Target Market(s)
B2B customer, including decision maker in food factories, chemical factories, etc.
Industry/Entity Type
Industry
Colors
Designer to choose colors to be used in the design.
Look and feel
Each slider illustrates characteristics of the customer's brand and the style your logo design should communicate.

```html
<!DOCTYPE html>
<html lang="en">
<head>
<meta charset="utf-8">
<title>Vernta Stationery Set</title>
<link href="https://fonts.googleapis.com/css2?family=Open+Sans:wght@400;600;800&display=swap" rel="stylesheet">
<style>
  :root {
    --green: #0e6e42;
    --green-dark: #0b5c37;
    --grey: #9aa3a8;
    --grey-light: #c9ced1;
    --paper: #ffffff;
    --ink: #3d4a44;
    --bg: #e9eaea;
  }
  * { box-sizing: border-box; margin: 0; padding: 0; }
  html, body { width: 1200px; height: 795px; overflow: hidden; }
  body {
    background: var(--bg);
    font-family: "Open Sans", Arial, sans-serif;
    color: var(--ink);
    position: relative;
  }
  .sheet { position: absolute; background: var(--paper); box-shadow: 0 2px 6px rgba(0,0,0,.12); overflow: hidden; }

  .wordmark { display: flex; align-items: center; gap: 6px; font-weight: 800; color: var(--green); letter-spacing: .5px; line-height: 1; }
  .wordmark .mark-square { background: currentColor; flex: none; }
  .wordmark.on-green { color: var(--paper); }

  .web-tab {
    position: absolute; right: 0; bottom: 0;
    background: var(--green); color: var(--paper);
    clip-path: polygon(9% 0, 100% 0, 100% 100%, 0 100%);
    display: flex; align-items: center; justify-content: flex-end;
    font-weight: 600; letter-spacing: .8px;
  }
  .web-tab.on-green { background: var(--paper); color: var(--green); }
  .base-line { position: absolute; left: 0; bottom: 0; height: 3px; background: var(--grey); }

  /* Letterhead */
  .letterhead { left: 300px; top: 34px; width: 300px; height: 424px; }
  .letterhead .wordmark { position: absolute; left: 22px; top: 24px; font-size: 22px; }
  .letterhead .wordmark .mark-square { width: 18px; height: 18px; }
  .contact-block { position: absolute; right: 18px; top: 30px; display: flex; gap: 12px; font-size: 5.5px; line-height: 1.7; }
  .contact-line { display: flex; align-items: center; gap: 3px; }
  .icon-dot { width: 7px; height: 7px; border-radius: 50%; background: var(--green); display: inline-flex; align-items: center; justify-content: center; }
  .icon-dot svg { width: 5px; height: 5px; }
  .letterhead .web-tab { width: 112px; height: 16px; font-size: 7px; padding-right: 10px; }
  .letterhead .base-line { width: 200px; }

  /* Presentation folder */
  .folder { left: 640px; top: 34px; width: 300px; height: 424px; background: var(--green); }
  .folder .wordmark { position: absolute; left: 40px; top: 178px; font-size: 46px; }
  .folder .wordmark .mark-square { width: 38px; height: 38px; }
  .folder .web-tab { width: 112px; height: 16px; font-size: 7px; padding-right: 10px; }

  /* Business cards */
  .card { width: 220px; height: 126px; left: 40px; }
  .card-front { top: 60px; }
  .card-front .wordmark { position: absolute; left: 14px; top: 44px; font-size: 17px; }
  .card-front .wordmark .mark-square { width: 14px; height: 14px; }
  .card-person { position: absolute; left: 128px; top: 24px; font-size: 6px; line-height: 1.5; }
  .card-person .name { font-weight: 600; color: var(--green); font-size: 7px; }
  .card-person .title { margin-bottom: 6px; }
  .card-front .web-tab { width: 96px; height: 12px; font-size: 5.5px; padding-right: 8px; }
  .card-front .base-line { width: 126px; height: 2px; }
  .card-back { top: 206px; background: var(--green); }
  .card-back .wordmark { position: absolute; left: 24px; top: 48px; font-size: 26px; }
  .card-back .wordmark .mark-square { width: 22px; height: 22px; }

  /* DL compliment sheet */
  .dl-sheet { left: 300px; top: 500px; width: 420px; height: 210px; }
  .dl-sheet .wordmark { position: absolute; left: 22px; top: 22px; font-size: 24px; }
  .dl-sheet .wordmark .mark-square { width: 20px; height: 20px; }
  .dl-sheet .address { position: absolute; left: 22px; top: 52px; font-size: 6.5px; }
  .dl-sheet .web-tab { width: 140px; height: 18px; font-size: 8px; padding-right: 12px; }
  .dl-sheet .base-line { width: 290px; }

  /* Envelope back */
  .envelope-back { left: 760px; top: 500px; width: 400px; height: 210px; }
  .envelope-back svg { display: block; }
</style>
</head>
<body>

  <!-- Letterhead -->
  <section class="sheet letterhead">
    <div class="wordmark"><span class="mark-square"></span>VERNTA</div>
    <div class="contact-block">
      <div>
        <div class="contact-line"><span class="icon-dot"><svg viewBox="0 0 10 10"><path d="M2 1l2 2-1 1.5a5 5 0 0 0 2.5 2.5L7 6l2 2-1.5 1.5C4.5 9 1 5.5.5 2.5z" fill="#fff"/></svg></span>000 000 000</div>
        <div class="contact-line"><span class="icon-dot"><svg viewBox="0 0 10 10"><rect x="1" y="2.5" width="8" height="5" fill="none" stroke="#fff"/><path d="M1 2.5l4 3 4-3" fill="none" stroke="#fff"/></svg></span>info@vernta.com</div>
      </div>
      <div>
        <div>street name, city name,</div>
        <div>state zip code</div>
      </div>
    </div>
    <div class="base-line"></div>
    <div class="web-tab">www.vernta.com</div>
  </section>

  <!-- Presentation folder -->
  <section class="sheet folder">
    <div class="wordmark on-green"><span class="mark-square"></span>VERNTA</div>
    <div class="web-tab on-green">www.vernta.com</div>
  </section>

  <!-- Business card, front -->
  <section class="sheet card card-front">
    <div class="wordmark"><span class="mark-square"></span>VERNTA</div>
    <div class="card-person">
      <div class="name">Employee Name</div>
      <div class="title">Job Title</div>
      <div class="contact-line"><span class="icon-dot"><svg viewBox="0 0 10 10"><path d="M2 1l2 2-1 1.5a5 5 0 0 0 2.5 2.5L7 6l2 2-1.5 1.5C4.5 9 1 5.5.5 2.5z" fill="#fff"/></svg></span>000 000 000</div>
      <div class="contact-line"><span class="icon-dot"><svg viewBox="0 0 10 10"><rect x="1" y="2.5" width="8" height="5" fill="none" stroke="#fff"/><path d="M1 2.5l4 3 4-3" fill="none" stroke="#fff"/></svg></span>info@vernta.com</div>
      <div class="contact-line"><span class="icon-dot"><svg viewBox="0 0 10 10"><path d="M5 9.5C3 7 2 5.5 2 4a3 3 0 0 1 6 0c0 1.5-1 3-3 5.5z" fill="#fff"/></svg></span>street name, city name, state zip code</div>
    </div>
    <div class="base-line"></div>
    <div class="web-tab">www.vernta.com</div>
  </section>

  <!-- Business card, back -->
  <section class="sheet card card-back">
    <div class="wordmark on-green"><span class="mark-square"></span>VERNTA</div>
  </section>

  <!-- DL compliment sheet -->
  <section class="sheet dl-sheet">
    <div class="wordmark"><span class="mark-square"></span>VERNTA</div>
    <div class="address">street name, city name, state zip code</div>
    <div class="base-line"></div>
    <div class="web-tab">www.vernta.com</div>
  </section>

  <!-- Envelope, back with flap -->
  <section class="sheet envelope-back">
    <svg width="400" height="210" viewBox="0 0 400 210">
      <path class="flap" d="M0 0H400V70Q400 84 386 84H14Q0 84 0 70Z" fill="var(--green)"/>
      <rect class="flap-square" x="188" y="28" width="24" height="24" fill="var(--grey)"/>
    </svg>
  </section>

</body>
</html>
```